Contractor Business Card Design

Looking to have a card made that has a bold description of (KITCHENS, BASEMENTS, BATHROOMS)

Definition and layers a plus

Contact info is;

Mark T. Ellery
Larkmoor, MN 55990
Cell: 612-555-0147
website: www.cobaltfinishworks.example
Email: cobaltfinishworksmn@mailbox.example

colors: red, black, gray, white

Contact Information for Business Card

Contact info is;

Mark T. Ellery
Larkmoor, MN 55990
Cell: 612-555-0147

Colors
ec1f27

Requirements
Must have
• Looking for layers and definition
Nice to have
• Cards are planned to be printed on plastic cards

```html
<!DOCTYPE html>
<html lang="en">
<head>
<meta charset="utf-8">
<title>Cobalt Finish Works – Business Card</title>
<link rel="stylesheet" href="https://fonts.googleapis.com/css2?family=Quicksand:wght@500;700&family=Arimo:wght@400&family=Playfair+Display:ital,wght@1,500&display=swap">
<style>
  :root {
    --red: #ec1f27;
    --ink: #1e1e20;
    --gray-text: #3a3a3c;
    --card-frost: #c9cacc;
    --card-frost-dark: #b4b5b8;
    --band: #2a2a2c;
    --panel: #f4f4f4;
    --backdrop: #e6e6e8;
  }
  * { box-sizing: border-box; margin: 0; padding: 0; }
  html, body { width: 1200px; height: 800px; overflow: hidden; }
  body {
    background: var(--backdrop);
    font-family: "Quicksand", sans-serif;
    color: var(--ink);
  }
  .sheet {
    position: relative;
    width: 1200px; height: 800px;
    display: flex; align-items: center; justify-content: center; gap: 40px;
  }
  .card {
    position: relative;
    width: 560px; height: 320px;
    border-radius: 18px;
    background: linear-gradient(160deg, var(--card-frost) 0%, var(--card-frost-dark) 100%);
    overflow: hidden;
  }

  /* Front */
  .brand { position: absolute; left: 40px; top: 36px; display: flex; align-items: center; gap: 14px; }
  .brand-dot { width: 46px; height: 46px; border-radius: 50%; background: var(--red); flex: none; }
  .brand-name { font-weight: 700; font-size: 26px; letter-spacing: 1px; text-transform: uppercase; line-height: 1.1; color: var(--ink); }
  .divider { position: absolute; left: 40px; top: 132px; width: 80px; height: 1.5px; background: var(--ink); }
  .person { position: absolute; left: 40px; top: 148px; }
  .person-name { font-weight: 700; font-size: 22px; line-height: 1.2; color: var(--red); text-transform: uppercase; letter-spacing: 0.5px; }
  .person-place { font-weight: 500; font-size: 16px; line-height: 1.3; color: var(--gray-text); margin-top: 2px; }
  .contacts { position: absolute; right: 30px; bottom: 26px; list-style: none; }
  .contacts li { display: flex; align-items: center; gap: 10px; font-weight: 500; font-size: 15px; color: var(--ink); line-height: 1.65; white-space: nowrap; }
  .contacts svg { width: 16px; height: 16px; flex: none; }

  /* Back */
  .band { position: absolute; left: 0; right: 0; top: 22px; bottom: 34px; background: var(--band); }
  .panel {
    position: absolute; left: 18px; right: 18px; top: 32px; bottom: 44px;
    background: var(--panel);
    display: grid; grid-template-columns: repeat(3, 1fr); gap: 14px;
    padding: 16px 16px 12px;
  }
  .service { display: flex; flex-direction: column; align-items: center; text-align: center; }
  .service-photo { width: 100%; height: 112px; border: 2px solid #6b5a48; flex: none; }
  .photo-basement { background: linear-gradient(135deg, #5b4636, #c59a60 60%, #e3c08a); }
  .photo-kitchen { background: linear-gradient(135deg, #d9dde0, #a9b1b6 55%, #7a6a5c); }
  .photo-install { background: linear-gradient(135deg, #6d6359, #9b9186 55%, #3b3836); }
  .service-title { font-family: "Playfair Display", serif; font-style: italic; font-weight: 500; font-size: 13px; margin: 8px 0 4px; color: var(--ink); }
  .service-text { font-family: "Arimo", sans-serif; font-size: 9.5px; line-height: 1.3; color: var(--gray-text); }
</style>
</head>
<body>
<main class="sheet">

  <section class="card card-front" aria-label="Card front">
    <div class="brand">
      <span class="brand-dot"></span>
      <span class="brand-name">Cobalt<br>Finish Works</span>
    </div>
    <div class="divider"></div>
    <div class="person">
      <p class="person-name">Mark T. Ellery</p>
      <p class="person-place">Larkmoor, MN 55990</p>
    </div>
    <ul class="contacts">
      <li>
        <svg viewBox="0 0 16 16"><rect x="4" y="1" width="8" height="14" rx="1.5" fill="none" stroke="var(--red)" stroke-width="1.5"/><circle cx="8" cy="12.5" r="0.9" fill="var(--red)"/></svg>
        612-555-0147
      </li>
      <li>
        <svg viewBox="0 0 16 16"><rect x="1.5" y="3.5" width="13" height="9" fill="none" stroke="var(--red)" stroke-width="1.5"/><path d="M1.5 3.5 8 9l6.5-5.5" fill="none" stroke="var(--red)" stroke-width="1.5"/></svg>
        cobaltfinishworksmn@mailbox.example
      </li>
      <li>
        <svg viewBox="0 0 16 16"><circle cx="8" cy="8" r="6.5" fill="none" stroke="var(--red)" stroke-width="1.5"/><path d="M1.5 8h13M8 1.5c-3 3.5-3 9.5 0 13M8 1.5c3 3.5 3 9.5 0 13" fill="none" stroke="var(--red)" stroke-width="1.2"/></svg>
        www.cobaltfinishworks.example
      </li>
    </ul>
  </section>

  <section class="card card-back" aria-label="Card back">
    <div class="band"></div>
    <div class="panel">
      <article class="service">
        <div class="service-photo photo-basement" role="img" aria-label="Photo of a finished basement with bar and media wall"></div>
        <h3 class="service-title">Basement Finish</h3>
        <p class="service-text">We strive to meet or exceed your expectations. We know the importance of deadlines, and you can depend on Cobalt Finish Works to get your home improvement job done on time and on budget.</p>
      </article>
      <article class="service">
        <div class="service-photo photo-kitchen" role="img" aria-label="Photo of a remodeled bright kitchen with island"></div>
        <h3 class="service-title">Kitchen Remodeling</h3>
        <p class="service-text">With 20 Years of experience, Cobalt Finish Works has the knowledge and ability to handle your home improvement project, no matter how big or small.</p>
      </article>
      <article class="service">
        <div class="service-photo photo-install" role="img" aria-label="Photo of a stone feature wall with mounted television and fireplace"></div>
        <h3 class="service-title">Fjordline Installations</h3>
        <p class="service-text">What we do isn't just a job; it's our passion. We have dedicated ourselves to making sure we do the best job possible because we want the best for you.</p>
      </article>
    </div>
  </section>

</main>
</body>
</html>
```